Web Design Project

We have a new games division in the company called "Bromo 7 Games" they are Cool and really different from anything else in the market. They are being sold to the international market and each product has a promotional video that goes with it and also QR coding on all packaging that will link to the website.
The site is to be fun and appeal to all age groups.

Target Market(s)

Children to Adults 6 -60

Requirements
Must have
• It must be cool and fun and show the quirie side of what we are doing. Images will be attached.
Headings:
Products
About Us
Awards
Large new Product area
Video show
News
Nice to have
• Bright and colorful and a bit of witt

```html
<!DOCTYPE html>
<html lang="en">
<head>
<meta charset="utf-8">
<title>Bromo 7 Games</title>
<link rel="stylesheet" href="https://fonts.googleapis.com/css2?family=Ubuntu:wght@400;500;700&family=Open+Sans:wght@400;600;700&display=swap">
<style>
:root{
  --black:#000;
  --red:#d7141c;
  --red-dark:#a80c12;
  --yellow:#f2ea2a;
  --yellow-light:#fdf98a;
  --white:#fff;
  --ink:#111;
  --grey:#9a9a9a;
  --link-yellow:#f6e81d;
}
*{margin:0;padding:0;box-sizing:border-box}
html,body{width:744px;height:1200px;overflow:hidden}
body{position:relative;font-family:"Open Sans",sans-serif;color:var(--ink);
  background:linear-gradient(90deg,#cfd2d6 0,#f3f3f5 23px,#fff 50%,#f3f3f5 721px,#cfd2d6 744px)}
.abs{position:absolute}
.page-backdrop{left:0;top:0;width:744px;height:1200px;background:radial-gradient(ellipse at 0 60%,#d9e6dc 0,transparent 35%),radial-gradient(ellipse at 100% 40%,#d8dbe2 0,transparent 30%)}
.content-column{left:23px;top:0;width:698px;height:1200px;background:#fbfbfc}

/* header */
.site-header{left:23px;top:0;width:698px;height:200px}
.header-bg{left:0;top:0}
.brand{left:20px;top:48px;display:flex;align-items:center;gap:8px;font-family:"Ubuntu",sans-serif;font-weight:700;font-size:25px;color:var(--white);line-height:1}
.brand-mark{width:18px;height:18px;background:var(--red)}
.search{left:404px;top:11px;width:155px;height:20px;background:var(--white);border-radius:3px;font-size:9px;color:var(--grey);padding:4px 9px}
.search svg{position:absolute;right:6px;top:3px}
.social{top:10px;width:22px;height:22px;border-radius:50%}
.social.s1{left:602px;background:#3b5ca0}
.social.s2{left:632px;background:#28a9e0}
.social.s3{left:662px;background:#f48120}
.main-nav{left:195px;top:77px;width:508px;height:36px;background:linear-gradient(var(--yellow-light),var(--yellow) 50%,#d8cf10);display:flex;align-items:center;font-family:"Ubuntu",sans-serif;font-weight:700;font-size:10.5px}
.main-nav a{color:var(--ink);text-decoration:none;position:absolute}
.nav-feature{left:231px;top:-5px;width:111px;height:46px;background:var(--red);border:2px solid var(--white);border-radius:4px;color:var(--white)!important;display:flex;align-items:center;justify-content:center;box-shadow:0 2px 4px rgba(0,0,0,.4)}

/* hero */
.hero-photo{left:23px;top:190px;width:698px;height:208px;background:linear-gradient(90deg,#e9e7ef 0,#f5f3f8 40%,#ecebf2 100%)}
.kids-photo{left:0;top:0;width:340px;height:208px;background:linear-gradient(100deg,#3f8fd1 0,#8fd14a 35%,#2fb4dc 60%,#f2cf32 85%,#eceaf1 100%);opacity:.85}
.board-photo{left:350px;top:40px;width:130px;height:100px;background:linear-gradient(135deg,#3d62a8,#d2282e);opacity:.8;border-radius:6px}
.hero-promo{left:537px;top:203px;width:166px;height:181px;background:#0c0c0c;border:2px solid var(--white);box-shadow:0 0 0 1px #bbb;padding:9px 8px 9px 10px;color:var(--white);font-size:8.8px;line-height:16px}
.hero-promo h2{font-family:"Ubuntu",sans-serif;font-weight:700;font-size:13px;color:var(--red);background:var(--white);display:inline-block;padding:0 3px;margin-bottom:5px;line-height:17px;text-transform:uppercase}
.hero-promo p+p{margin-top:16px}

/* sections */
.section-title{font-family:"Ubuntu",sans-serif;font-weight:700;font-size:20px;text-transform:uppercase;line-height:1;color:var(--black);white-space:nowrap}
.section-title .accent{color:var(--red)}
.welcome-title{left:40px;top:421px}
.welcome-copy{left:40px;top:455px;width:466px;font-size:8px;line-height:16px;color:#222}
.welcome-copy p+p{margin-top:16px}
.featured-photo{left:525px;top:432px;width:169px;height:173px;background:linear-gradient(135deg,#c4111b 0,#e03a3a 40%,#181818 45%,#333 80%,#cfd0dc 100%);border:1px solid #ccc}
.btn-read{left:431px;top:599px;width:65px;height:20px;background:linear-gradient(#444,#111);color:var(--white);font-size:8.5px;font-weight:600;border-radius:3px;display:flex;align-items:center;justify-content:center;border:1px solid #000;text-decoration:none}
.divider{left:38px;top:627px;width:668px;height:4px;border-top:1px dashed #c9c9c9;border-bottom:1px dashed #c9c9c9}

.category-title{left:40px;top:647px}
.product-grid{left:38px;top:678px;width:389px;height:324px;border:1px solid #bdbdbd;background:var(--white)}
.product-card{width:120px}
.product-img{height:68px;background:linear-gradient(135deg,#e8eaf2,#d2d6e6);border:1px solid #dadada;display:flex;align-items:center;justify-content:center}
.product-img span{display:block;width:90px;height:34px;background:linear-gradient(90deg,#3a66b8,#d7262d,#f2c21e,#3a66b8);opacity:.7;border-radius:4px}
.product-meta{display:flex;justify-content:space-between;align-items:center;margin-top:7px;font-family:"Ubuntu",sans-serif;font-weight:700;font-size:10px}
.price{background:var(--red);color:var(--white);font-size:13px;padding:1px 4px;border-radius:3px;line-height:18px}
.product-desc{font-size:6.8px;line-height:12px;margin-top:7px;padding-left:2px;color:#222}

.video-title{left:461px;top:647px}
.video-player{left:461px;top:683px;width:236px;height:158px;background:#111;border:1px solid #999}
.video-frame{left:0;top:0;width:234px;height:143px;background:linear-gradient(135deg,#2a2f6a 0,#c21d25 35%,#1a1a1a 60%,#5b82c9 100%)}
.play-btn{left:96px;top:53px}
.video-bar{left:0;top:143px;width:234px;height:13px}
.mascot{left:594px;top:893px;width:126px;height:152px;background:linear-gradient(180deg,#f0e5d8 0,#f29e2c 25%,#8a5fb2 60%,#e8e8ef 100%);border-radius:40px 40px 10px 10px;opacity:.85}

/* footer */
.footer-bg{left:23px;top:1020px}
.footer-links{top:1066px;list-style:none;font-size:8.5px;line-height:16px;color:var(--white)}
.footer-links.c1{left:64px}.footer-links.c2{left:152px}.footer-links.c3{left:245px}
.footer-brand{left:390px;top:1082px;width:70px;display:flex;align-items:flex-start;gap:5px;font-family:"Ubuntu",sans-serif;font-weight:700;font-size:11px;line-height:13px;color:var(--white)}
.footer-brand i{flex:none;width:9px;height:9px;margin-top:2px;background:var(--red);display:block}
.footer-contact{left:473px;top:1083px;font-size:11px;line-height:20px;color:var(--white);white-space:nowrap}
.footer-contact a{color:var(--link-yellow);text-decoration:none}
.legal-bar{left:23px;top:1178px;width:698px;height:22px;background:var(--red);color:var(--white);font-size:8px;text-align:right;padding:6px 12px}
</style>
</head>
<body>
<div class="abs page-backdrop" role="img" aria-label="Soft decorative swirl pattern behind the page"></div>
<div class="abs content-column"></div>

<header class="abs site-header">
  <svg class="abs header-bg" width="698" height="200" viewBox="0 0 698 200" aria-hidden="true">
    <path d="M0 0H698V196L680 182 660 170 630 166 600 174 570 168 540 176 500 170 470 178 430 170 390 176 350 168 310 176 270 170 230 178 190 170 150 176 110 168 80 174 50 166 20 172 0 168Z" fill="var(--red)"/>
    <path d="M0 0H698V190L680 176 660 164 630 160 600 168 570 162 540 170 500 164 470 172 430 164 390 170 350 162 310 170 270 164 230 172 190 164 150 170 110 162 80 168 50 160 20 166 0 162Z" fill="var(--black)"/>
  </svg>
  <div class="abs brand"><span class="brand-mark"></span>Bromo 7 Games</div>
  <div class="abs search">search
    <svg width="12" height="12" viewBox="0 0 12 12" aria-hidden="true"><circle cx="5" cy="5" r="3.5" fill="none" stroke="#bbb" stroke-width="1.5"/><path d="M7.5 7.5 11 11" stroke="#bbb" stroke-width="1.5"/></svg>
  </div>
  <span class="abs social s1" aria-label="Social link"></span>
  <span class="abs social s2" aria-label="Social link"></span>
  <span class="abs social s3" aria-label="Social link"></span>
  <nav class="abs main-nav">
    <a href="#" style="left:26px">Products</a>
    <a href="#" style="left:98px">About Us</a>
    <a href="#" style="left:174px">Awards</a>
    <a href="#" class="nav-feature">Large new &nbsp;Product</a>
    <a href="#" style="left:366px">V ideo show</a>
    <a href="#" style="left:448px">News</a>
  </nav>
</header>

<section class="abs hero-photo">
  <div class="abs kids-photo" role="img" aria-label="Photo of four smiling children lying on the floor"></div>
  <div class="abs board-photo" role="img" aria-label="Photo of the red and blue tic tac toe game board"></div>
</section>
<aside class="abs hero-promo">
  <h2>Battle every spot!</h2>
  <p>Finaly, a Tic Tac Toe game where the fun doesn't end with the first three-in-a-rowand the games are a thing of the past.</p>
  <p>In TAC Blitz TOE, you battle your opponent for every spot, by playing higher numbers on</p>
</aside>

<h1 class="abs section-title welcome-title"><span class="accent">Welcome to Bromo 7</span> Games</h1>
<div class="abs welcome-copy">
  <p>Finaly, a Tic Tac Toe game where the fun doesn't end with the first three-in-a-rowand the games are a thing of the past. &nbsp;In TAC Blitz TOE, you battle your opponent for every spot, by playing higher numbers on top of lower numbers. Finaly, a Tic Tac Toe game where the fun doesn't end with the first three-in-a-rowand the games are a thing of the past. &nbsp;In TAC Blitz TOE, you battle your opponent for every spot, by playing higher numbers on top of lower numbers. Finaly, a Tic Tac Toe game where the fun doesn't end with the first three-in-a-rowand the games are a thing of the past. &nbsp;In TAC Blitz TOE, you battle your opponent for every spot, by playing higher numbers on top of lower numbers.</p>
  <p>Finaly, a Tic Tac Toe game where the fun doesn't end with the first three-in-a-rowand the games are a thing of the past. &nbsp;In TAC Blitz TOE, you battle your opponent for every spot, by playing higher numbers on top of lower numbers.</p>
</div>
<div class="abs featured-photo" role="img" aria-label="Flick Fest game artwork with a crowd silhouette"></div>
<a class="abs btn-read" href="#">READ MORE</a>
<div class="abs divider"></div>

<h2 class="abs section-title category-title"><span class="accent">Browse by</span> Category</h2>
<div class="abs product-grid">
  <article class="abs product-card" style="left:6px;top:6px"><div class="product-img" role="img" aria-label="Game tiles product photo"><span></span></div><div class="product-meta"><span>PRODUT 1</span><span class="price">$19.00</span></div><p class="product-desc">Finaly, a Tic Tac Toe game where the fun doesn't end with the first three-in-a-rowand the games are a thing of the past.</p></article>
  <article class="abs product-card" style="left:135px;top:6px"><div class="product-img" role="img" aria-label="Game tiles product photo"><span></span></div><div class="product-meta"><span>PRODUT 1</span><span class="price">$19.00</span></div><p class="product-desc">Finaly, a Tic Tac Toe game where the fun doesn't end with the first three-in-a-rowand the games are a thing of the past.</p></article>
  <article class="abs product-card" style="left:263px;top:6px"><div class="product-img" role="img" aria-label="Game tiles product photo"><span></span></div><div class="product-meta"><span>PRODUT 1</span><span class="price">$19.00</span></div><p class="product-desc">Finaly, a Tic Tac Toe game where the fun doesn't end with the first three-in-a-rowand the games are a thing of the past.</p></article>
  <article class="abs product-card" style="left:6px;top:163px"><div class="product-img" role="img" aria-label="Game tiles product photo"><span></span></div><div class="product-meta"><span>PRODUT 1</span><span class="price">$19.00</span></div><p class="product-desc">Finaly, a Tic Tac Toe game where the fun doesn't end with the first three-in-a-rowand the games are a thing of the past.</p></article>
  <article class="abs product-card" style="left:135px;top:163px"><div class="product-img" role="img" aria-label="Game tiles product photo"><span></span></div><div class="product-meta"><span>PRODUT 1</span><span class="price">$19.00</span></div><p class="product-desc">Finaly, a Tic Tac Toe game where the fun doesn't end with the first three-in-a-rowand the games are a thing of the past.</p></article>
  <article class="abs product-card" style="left:263px;top:163px"><div class="product-img" role="img" aria-label="Game tiles product photo"><span></span></div><div class="product-meta"><span>PRODUT 1</span><span class="price">$19.00</span></div><p class="product-desc">Finaly, a Tic Tac Toe game where the fun doesn't end with the first three-in-a-rowand the games are a thing of the past.</p></article>
</div>

<h2 class="abs section-title video-title"><span class="accent">Featured</span> Video</h2>
<div class="abs video-player">
  <div class="abs video-frame" role="img" aria-label="Video still of the Flick Fest game box with toy guitars"></div>
  <svg class="abs play-btn" width="40" height="40" viewBox="0 0 40 40" aria-hidden="true"><circle cx="20" cy="20" r="18" fill="#222" stroke="#fff" stroke-width="2.5"/><path d="M15 11 29 20 15 29Z" fill="#fff"/></svg>
  <svg class="abs video-bar" width="234" height="13" viewBox="0 0 234 13" aria-hidden="true"><rect width="234" height="13" fill="#1c1c1c"/><path d="M4 4h3l3-2v9L7 9H4Z" fill="#ccc"/><rect x="14" y="5.5" width="30" height="2" fill="#aaa"/><path d="M54 3 60 6.5 54 10Z" fill="#ccc"/><rect x="66" y="5.5" width="120" height="2" fill="#666"/><rect x="66" y="5.5" width="56" height="2" fill="var(--red)"/><circle cx="122" cy="6.5" r="3" fill="#ddd"/><text x="192" y="9" font-size="5" fill="#ccc" font-family="Open Sans,sans-serif">3:12/3:00</text><rect x="222" y="3" width="7" height="7" fill="none" stroke="#ccc"/></svg>
</div>
<div class="abs mascot" role="img" aria-label="Illustration of a clown mascot holding a plunger"></div>

<footer>
  <svg class="abs footer-bg" width="698" height="158" viewBox="0 0 698 158" aria-hidden="true">
    <path d="M0 18 40 10 80 16 120 8 170 14 220 6 270 12 320 4 370 12 420 6 470 14 520 6 570 14 620 8 698 0V158H0Z" fill="var(--black)"/>
  </svg>
  <ul class="abs footer-links c1"><li>About us</li><li>Profile</li><li>Services</li><li>Lorem ipsum</li><li>Lorem</li><li>Ipsum</li></ul>
  <ul class="abs footer-links c2"><li>About us</li><li>Profile</li><li>Services</li><li>Lorem ipsum</li><li>Lorem</li><li>Ipsum</li></ul>
  <ul class="abs footer-links c3"><li>About us</li><li>Profile</li><li>Services</li><li>Lorem ipsum</li><li>Lorem</li><li>Ipsum</li></ul>
  <div class="abs footer-brand"><i></i><span>Bromo 7<br>Games</span></div>
  <p class="abs footer-contact">For distributor enquirines.<br>contact &nbsp;<a href="mailto:sam@thefunworks.com">sam@thefunworks.com</a></p>
  <div class="abs legal-bar">All rights reserved @ Bromo7Games</div>
</footer>
</body>
</html>
```